Expense Tracker App for Young Adults

I need a mobile app designer to design an app UI for me. It is for an expense tracker app. I’ve attached a mind map of the various screens and features of the app.

I would like to see designs for this app which is targeted towards young adults (late teens & early 20s) just starting their career who want to plan their budgets and track their expenses.
Updates

Hello designers! I'm conscious that this is not a guaranteed project, so I can understand that some of you might be apprehensive. Just wanted to let you know that I'm willing to see your initial drafts that show your direction and theme for design. You don't have to design the whole app. In fact, it's better if you share your initial design ideas so that we can have a discussion and I can give my input. If I see some good initial designs, I will be happy to make this a guaranteed project. I'm simply being cautious since I'm bootstrapping this and funding out of my own pocket. Thank you for your understanding!

Target Market(s)

Young adults who are just starting their careers, late teens and early 20s.

Font styles to use
Sans Serif

Requirements
Must have
• Ease of use, smart and sleek, a guided setup wizard which will help users setup their account after signing up.
Should not have
• Clunky

```html
<!DOCTYPE html>
<html lang="en">
<head>
<meta charset="utf-8">
<title>BDG - UP — App Screens</title>
<link rel="stylesheet" href="https://fonts.googleapis.com/css2?family=Rajdhani:wght@400;500;600;700&display=swap">
<style>
  :root{
    --canvas:#aaaaaa;
    --header:#465a66;
    --accent:#f15524;
    --paper:#fcecea;
    --footer:#5c5c5c;
    --field:#ffffff;
    --ink:#111111;
    --field-ink:#444444;
    --yellow:#e2c31b;
    --green:#0a6e3a;
    --blue:#0e4d94;
    --white:#ffffff;
  }
  *{box-sizing:border-box;margin:0;padding:0}
  html,body{width:1200px;height:832px;overflow:hidden}
  body{background:var(--canvas);font-family:"Rajdhani",sans-serif;position:relative}

  .screen{position:absolute;background:var(--paper);overflow:hidden}
  .screen--settings{left:88px;top:87px;width:303px;height:657px;border-radius:30px}
  .screen--expense{left:449px;top:68px;width:325px;height:573px}
  .screen--income{left:811px;top:68px;width:325px;height:573px}

  .app-header{position:absolute;left:0;top:0;width:100%}
  .app-header svg{display:block;width:100%;height:100%}
  .screen--settings .app-header{height:130px}
  .screen--expense .app-header,.screen--income .app-header{height:100px}
  .app-name{position:absolute;left:0;width:100%;text-align:center;color:var(--white);
    font-weight:700;font-size:37px;letter-spacing:1px;line-height:1}
  .screen--settings .app-name{top:56px;font-size:35px}
  .screen--expense .app-name,.screen--income .app-name{top:18px}

  .screen-title{position:absolute;left:0;width:100%;text-align:center;color:var(--ink);font-weight:700;line-height:40px}
  .screen--settings .screen-title{top:166px;font-size:34px;letter-spacing:1px}
  .screen--expense .screen-title{top:143px;font-size:38px}
  .screen--income .screen-title{top:143px;font-size:38px}

  .setting-btn{position:absolute;left:6px;width:291px;height:73px;border-radius:5px;
    display:flex;align-items:center;padding-left:11px;color:var(--white);font-size:19px;font-weight:600}
  .setting-btn .icon{width:48px;height:48px;border-radius:50%;background:var(--white);
    display:flex;align-items:center;justify-content:center;margin-right:12px;flex:none}
  .setting-btn--notify{top:225px;background:var(--yellow)}
  .setting-btn--currency{top:313px;background:var(--green)}
  .setting-btn--language{top:400px;background:var(--blue)}
  .setting-btn--logout{top:488px;background:var(--accent)}
  .dollar{color:var(--green);font-size:32px;font-weight:700;line-height:1}

  .field{position:absolute;left:21px;width:284px;height:49px;background:var(--field);
    display:flex;align-items:center;padding:0 21px;color:var(--field-ink);font-size:14.5px;font-weight:500;
    box-shadow:0 1px 2px rgba(0,0,0,.05)}
  .field--select::after{content:"";position:absolute;right:22px;top:22px;
    border-left:5px solid transparent;border-right:5px solid transparent;border-top:5px solid #222}
  .save-btn{position:absolute;left:21px;top:371px;width:284px;height:49px;background:var(--accent);
    color:var(--white);font-weight:700;font-size:20px;display:flex;align-items:center;justify-content:center;letter-spacing:.5px}

  .app-footer{position:absolute;left:0;bottom:0;width:100%;height:59px;background:var(--footer);
    color:var(--white);font-size:14.5px;display:flex;align-items:center;justify-content:center;font-weight:500}
  .screen--settings .app-footer{height:59px;padding-bottom:6px}
</style>
</head>
<body>

  <!-- Settings screen -->
  <section class="screen screen--settings">
    <div class="app-header">
      <svg viewBox="0 0 325 100" preserveAspectRatio="none">
        <path d="M0 0H325V84C280 96 230 100 190 93C150 86 120 80 80 80C50 80 20 84 0 88Z" fill="var(--header)"/>
        <path d="M0 88C20 83 50 79 82 80C115 81 145 86 165 90C130 98 90 100 55 98C30 96 12 94 0 92Z" fill="var(--accent)"/>
      </svg>
    </div>
    <h1 class="app-name">BDG - UP</h1>
    <h2 class="screen-title">SETTINGS</h2>

    <div class="setting-btn setting-btn--notify">
      <span class="icon"><svg width="22" height="22" viewBox="0 0 24 24"><path d="M12 2a2 2 0 0 1 2 2v.6A6.5 6.5 0 0 1 18.5 11v4l2 3H3.5l2-3v-4A6.5 6.5 0 0 1 10 4.6V4a2 2 0 0 1 2-2zm-2.5 17h5a2.5 2.5 0 0 1-5 0z" fill="var(--yellow)"/></svg></span>
      Notification Preferences
    </div>
    <div class="setting-btn setting-btn--currency">
      <span class="icon"><span class="dollar">$</span></span>
      Currency
    </div>
    <div class="setting-btn setting-btn--language">
      <span class="icon"><svg width="26" height="26" viewBox="0 0 24 24"><circle cx="12" cy="12" r="11" fill="var(--blue)"/><path d="M6 7c2-1 4 0 4 2s-2 2-1 4 3 1 3 4-2 3-3 2c-1-2-3-3-3-6S4 8 6 7zM14 5c2 0 4 1 5 3-1 1-3 0-4 1s-2-1-1-2z" fill="var(--white)"/></svg></span>
      Language
    </div>
    <div class="setting-btn setting-btn--logout">
      <span class="icon"><svg width="26" height="24" viewBox="0 0 26 24"><path d="M10 4H5a2 2 0 0 0-2 2v12a2 2 0 0 0 2 2h5" fill="none" stroke="var(--accent)" stroke-width="3"/><path d="M9 9h8V4l8 8-8 8v-5H9z" fill="var(--accent)"/></svg></span>
      Logout
    </div>

    <footer class="app-footer">© 2020 BDG - UP. All rights reserved.Privacy</footer>
  </section>

  <!-- Add expense screen -->
  <section class="screen screen--expense">
    <div class="app-header">
      <svg viewBox="0 0 325 100" preserveAspectRatio="none">
        <path d="M0 0H325V84C280 96 230 100 190 93C150 86 120 80 80 80C50 80 20 84 0 88Z" fill="var(--header)"/>
        <path d="M0 88C20 83 50 79 82 80C115 81 145 86 165 90C130 98 90 100 55 98C30 96 12 94 0 92Z" fill="var(--accent)"/>
      </svg>
    </div>
    <h1 class="app-name">BDG - UP</h1>
    <h2 class="screen-title">Add New Expense</h2>
    <div class="field field--select" style="top:222px">Scan Receipt</div>
    <div class="field field--select" style="top:281px">Scan credit card Statement</div>
    <div class="field field--select" style="top:340px">Type manually</div>
    <div class="field" style="top:399px">Voice Command</div>
    <footer class="app-footer">© 2020 BDG - UP. All rights reserved.Privacy</footer>
  </section>

  <!-- Auto income screen -->
  <section class="screen screen--income">
    <div class="app-header">
      <svg viewBox="0 0 325 100" preserveAspectRatio="none">
        <path d="M0 0H325V84C280 96 230 100 190 93C150 86 120 80 80 80C50 80 20 84 0 88Z" fill="var(--header)"/>
        <path d="M0 88C20 83 50 79 82 80C115 81 145 86 165 90C130 98 90 100 55 98C30 96 12 94 0 92Z" fill="var(--accent)"/>
      </svg>
    </div>
    <h1 class="app-name">BDG - UP</h1>
    <h2 class="screen-title">Auto Income<br>Credit</h2>
    <div class="field" style="top:253px">Fixed Amount preset</div>
    <div class="field" style="top:312px">Variable amount field empty</div>
    <div class="save-btn">SAVE</div>
    <footer class="app-footer">© 2020 BDG - UP. All rights reserved.Privacy</footer>
  </section>

</body>
</html>
```